Private Investment Firm Needs PowerPoint Presentation Template

Design PowerPoint template, take Ridgefell-submitted rough presentation draft, and drop it into new template. See attached Project Brief file for more detail.
Updates

Some decent designs have been submitted but they seem to lack the understanding of our target markets. I am hopeful that more time and feedback will result in better results.

Target Market(s)

Private company owners and intermediaries.

Font styles to use
Serif

Colors
3176b5

Requirements
Must have
• See attached Project Brief.
Nice to have
Should not have
• No B2C fluff--this is a B2B project.

```html
<!DOCTYPE html>
<html lang="en">
<head>
<meta charset="utf-8">
<title>Ridgefell Capital – Introduction to Non-Control Capital</title>
<link rel="stylesheet" href="https://fonts.googleapis.com/css2?family=Arimo:wght@400;700&family=Tinos:wght@400;700&family=Open+Sans:wght@300&family=Oswald:wght@500;700&display=swap">
<style>
:root{
  --brand:#1a6fc2;
  --navy:#274a6c;
  --mist:#dce5ef;
  --ink:#1e1e1e;
  --mark-ink:#3b3b3b;
  --grey-slide:#7f7f7f;
  --frame:#c9c9c9;
  --white:#ffffff;
}
*{box-sizing:border-box;margin:0;padding:0}
html,body{width:1200px;height:454px;overflow:hidden;background:var(--frame)}
.deck{position:relative;width:1200px;height:454px}
.slide{position:absolute;width:394px;height:222px;background:var(--white);overflow:hidden}
.s1{left:3px;top:3px}.s2{left:402px;top:3px}.s3{left:802px;top:3px}
.s4{left:3px;top:229px}.s5{left:402px;top:229px}.s6{left:802px;top:229px}

/* cover */
.cover-panel{position:absolute;left:322px;top:0;width:72px;height:222px;
  background:linear-gradient(135deg,var(--navy) 0%,#3a6c98 55%,var(--navy) 100%)}
.cover-brand{position:absolute;left:64px;top:32px;display:flex;align-items:center;gap:10px}
.brand-square{width:40px;height:40px;background:var(--brand)}
.brand-name{font-family:"Tinos",serif;font-weight:400;font-size:23px;letter-spacing:1px;color:var(--mark-ink);line-height:1}
.cover-title{position:absolute;right:162px;top:128px;text-align:right;
  font-family:"Arimo",sans-serif;font-weight:700;color:var(--brand);
  font-size:25px;line-height:20.5px;letter-spacing:-1px}
.cover-block{position:absolute;left:237px;top:128px;width:113px;height:61px;background:var(--brand)}
.cover-sub{position:absolute;right:79px;top:193px;text-align:right;
  font-family:"Arimo",sans-serif;font-size:8.6px;line-height:10px;color:var(--ink)}
.cover-date{position:absolute;left:6px;top:207px;font-family:"Tinos",serif;font-weight:700;font-size:7px;color:var(--ink)}

/* content slides */
.side-panel{position:absolute;left:322px;top:0;width:72px;height:222px;background:var(--mist)}
.title-bar{position:absolute;left:9px;top:1px;width:10px;height:33px;background:var(--brand)}
.slide-title{position:absolute;left:22px;top:24px;font-family:"Arimo",sans-serif;font-weight:700;
  color:var(--brand);font-size:12.6px;line-height:14px}
.bullets{position:absolute;left:20px;top:45px;width:294px;font-family:"Tinos",serif;
  font-size:8.8px;line-height:10px;color:var(--ink);list-style:none}
.bullets>li{position:relative;padding-left:9px;margin-bottom:4px}
.bullets>li::before{content:"•";position:absolute;left:0}
.bullets ul{list-style:none;margin-top:1px}
.bullets ul li{position:relative;padding-left:16px;font-size:8px;line-height:11px}
.bullets ul li::before{content:"•";position:absolute;left:7px}
.bullets u{font-weight:700}
.footer-brand{position:absolute;left:5px;top:203px;display:flex;align-items:center;gap:4px}
.footer-square{width:9px;height:9px;background:var(--brand)}
.footer-name{font-family:"Tinos",serif;font-size:8px;letter-spacing:1px;color:var(--mark-ink)}
.footer-line{position:absolute;left:73px;top:207px;width:287px;height:6px;background:var(--brand)}
.footer-tab{position:absolute;left:377px;top:203px;width:17px;height:14px;background:var(--brand)}

/* quote slides */
.quote{display:flex;flex-direction:column;align-items:center;text-align:center;color:var(--white)}
.quote.blue{background:var(--brand)}
.quote.grey{background:var(--grey-slide)}
.q-mark{font-family:"Oswald",sans-serif;font-weight:700;font-size:72px;line-height:62px;height:26px;margin-top:12px;overflow:hidden}
.q-close{margin-top:6px}
.q-text{font-family:"Open Sans",sans-serif;font-weight:300;font-size:10.4px;line-height:13.8px;
  width:282px;margin-top:11px}
.q-author{font-family:"Oswald",sans-serif;font-weight:500;font-size:10px;line-height:14px;margin-top:8px}
.quote.grey .q-author{color:#111}
</style>
</head>
<body>
<main class="deck">

  <section class="slide s1">
    <div class="cover-brand">
      <div class="brand-square"></div>
      <span class="brand-name">Ridgefell Capital</span>
    </div>
    <h1 class="cover-title">INTRODUCTION TO<br>NON-CONTROL<br>CAPITAL</h1>
    <div class="cover-block"></div>
    <p class="cover-sub">The Lower Middle Market Private Company Strategy for Raising Capital<br>While Maintaining Business Control</p>
    <p class="cover-date">Fall 2018</p>
    <div class="cover-panel" role="img" aria-label="Navy side panel with large decorative graphic"></div>
  </section>

  <section class="slide s2">
    <div class="side-panel" role="img" aria-label="Faint decorative graphic"></div>
    <div class="title-bar"></div>
    <h2 class="slide-title">INTRODUCTION</h2>
    <ul class="bullets" style="top:46px">
      <li>Private company owners have traditionally considered two capital raising options:
        <ul><li>Borrow from a local bank, or</li><li>Sell most or all of the company to a change-of-control investor (aka Buyout firm)</li></ul></li>
      <li>An alternative most have not considered is the raising of Non-Control Capital, or capital that is invested into the business yet allows those same owners to retain controlling interest in their company</li>
      <li>Non-Control Capital is not appropriate for every private company owner but neither is a Change-of-Control sale</li>
      <li>The key is to determine what the business and owners require, and then partner with an investor best aligned with those needs so that long-term company growth, and personal goals, can both be achieved</li>
    </ul>
    <div class="footer-brand"><div class="footer-square"></div><span class="footer-name">RIDGEFELL</span></div>
    <div class="footer-line"></div><div class="footer-tab"></div>
  </section>

  <section class="slide s3">
    <div class="side-panel" role="img" aria-label="Faint decorative graphic"></div>
    <div class="title-bar"></div>
    <h2 class="slide-title">WHAT IS NON-CONTROL CAPITAL?</h2>
    <ul class="bullets" style="top:54px">
      <li>Non-Control Capital is an investment which is primarily used for the ongoing operation and/or growth of a business but <u>also</u> allows the current owners to retain:
        <ul><li>Control of the business economics</li><li>Control of the business operations</li><li>Control of strategy and key decision making</li><li>Control of the Board of Directors</li></ul></li>
      <li style="margin-top:9px">Requires the alignment of management incentives with ownership</li>
      <li style="margin-top:11px">In essence, a company receives the capital it needs to implement its business plans but owners continue to retain ultimate control</li>
    </ul>
    <div class="footer-brand"><div class="footer-square"></div><span class="footer-name">RIDGEFELL</span></div>
    <div class="footer-line"></div><div class="footer-tab"></div>
  </section>

  <section class="slide s4">
    <div class="side-panel" role="img" aria-label="Faint decorative graphic"></div>
    <div class="title-bar"></div>
    <h2 class="slide-title" style="top:22px">WHEN IS A NON-CONTROL TRANSACTION<br>APPROPRIATE?</h2>
    <ul class="bullets" style="top:60px;width:300px">
      <li>The company has opportunities to expand but requires capital to do so</li>
      <li>At least one active owner <u>is not</u> close to retirement</li>
      <li>The company is not in a turnaround situation</li>
      <li>Family members may work in the business and want to continue</li>
      <li>Owners care about keeping the business in their family name (legacy)</li>
      <li>Liquidity (dividend) is not the major use of the invested capital</li>
      <li>Owners are sensitive to utilizing too much debt</li>
      <li>Companies require more than just capital:
        <ul><li>They may also need operational, marketing, financial, and/or technology counsel</li></ul></li>
    </ul>
    <div class="footer-brand"><div class="footer-square"></div><span class="footer-name">RIDGEFELL</span></div>
    <div class="footer-line"></div><div class="footer-tab"></div>
  </section>

  <section class="slide s5 quote blue">
    <div class="q-mark">&ldquo;</div>
    <p class="q-text">OUR COMPANY HAD SEVERAL BUSINESS OPPORTUNITIES BUT I NEEDED OUTSIDE CAPITAL TO TAKE ADVANTAGE OF THEM. WHY WOULD I CEDE CONTROL OF MY BUSINESS WHEN WE WERE AT THE EXACT POINT WHEN RAISING OUTSIDE CAPITAL WOULD ALLOW ME TO ACCELERATE GROWTH AND ACHIEVE MY LIFE-LONG BUSINESS AND PERSONAL GOALS?!</p>
    <div class="q-mark q-close">&rdquo;</div>
    <p class="q-author">MARK DELANEY<br>CEO<br>THE HARBOR LINE GROUP</p>
  </section>

  <section class="slide s6 quote grey">
    <div class="q-mark">&ldquo;</div>
    <p class="q-text">OUR COMPANY HAD SEVERAL BUSINESS OPPORTUNITIES BUT I NEEDED OUTSIDE CAPITAL TO TAKE ADVANTAGE OF THEM. WHY WOULD I CEDE CONTROL OF MY BUSINESS WHEN WE WERE AT THE EXACT POINT WHEN RAISING OUTSIDE CAPITAL WOULD ALLOW ME TO ACCELERATE GROWTH AND ACHIEVE MY LIFE-LONG BUSINESS AND PERSONAL GOALS?!</p>
    <div class="q-mark q-close">&rdquo;</div>
    <p class="q-author">MARK DELANEY<br>CEO<br>THE HARBOR LINE GROUP</p>
  </section>

</main>
</body>
</html>
```